VELMORAN RECORDS
New independent record label
VELMORAN RECORDS -
Creative Brief
www.velmoranrecords.co.uk
independent record label
we are open to your thoughts and designs.
Modern
Red used in the logo for the background colour
below header
www.plintonrecords.co.uk
www.quaystreetjournal.com
www.brindlewick.co.uk
we would like a banner in the header that slideshows the signed artists with a small text biography.

```html
<!DOCTYPE html>
<html lang="en">
<head>
<meta charset="utf-8">
<title>Velmoran Records</title>
<link rel="stylesheet" href="https://fonts.googleapis.com/css2?family=Cinzel:wght@400;700&family=Arimo:wght@400;700&display=swap">
<style>
:root{
  --black:#0b0b0b;
  --dark:#1c1c1e;
  --panel:#2a2a2c;
  --grey:#8d8d90;
  --light:#d9d9db;
  --white:#f4f4f4;
  --red:#c4141a;
  --red-deep:#5a0608;
  --red-text:#e23a3a;
  --text:#bdbdbd;
  --mark:#5a5a5c;
}
*{margin:0;padding:0;box-sizing:border-box}
html,body{width:1200px;height:1027px;overflow:hidden;background:var(--black)}
body{font-family:"Arimo",Arial,sans-serif;color:var(--text);position:relative}
.page{position:absolute;inset:0;background:
  radial-gradient(ellipse 70% 14% at 50% 46%,#b3141a 0%,#6c0a0d 55%,transparent 100%),
  linear-gradient(#0c0c0c 0,#141414 37%,#3a0608 40%,#8a0e12 46%,#3a0608 53%,#1e1e20 57%,#232325 100%)}
.abs{position:absolute}

/* top navigation */
.nav{left:173px;top:0;width:899px;height:50px;display:flex}
.nav a{flex:1;display:flex;align-items:center;justify-content:center;color:var(--white);text-decoration:none;font-size:15px;
  background:linear-gradient(#3e3e40,#161617);border-left:1px solid #555;border-radius:0 0 8px 8px;text-transform:uppercase}
.nav a.active{background:linear-gradient(#8c8c8e,#3b3b3d)}

/* login */
.login{left:713px;top:62px;display:flex;gap:12px;align-items:center}
.login .field{width:96px;height:14px;background:#2f2f31;border:1px solid #5a5a5c;font-size:8px;color:#888;padding-left:5px;line-height:12px}
.login .btn{width:48px;height:14px;background:var(--red);font-size:7px;color:#fff;text-align:center;line-height:14px;text-transform:uppercase}

/* brand */
.brand{left:190px;top:84px;display:flex;align-items:center;gap:20px}
.brand .mark{width:108px;height:108px;border-radius:50%;background:var(--mark)}
.brand .name{font-family:"Arimo",Arial,sans-serif;font-weight:700;color:var(--white);font-size:34px;letter-spacing:1px;line-height:1}
.brand .name span{display:block;font-size:11px;letter-spacing:6px;margin-top:4px;margin-left:120px}

.search{left:947px;top:161px;width:108px;height:14px;background:#2f2f31;border:1px solid #5a5a5c;font-size:8px;color:#888;padding-left:5px;line-height:12px}

/* slideshow */
.slideshow{left:173px;top:195px;width:894px;height:251px;background:rgba(70,70,72,.75);border:1px solid #666;border-radius:10px}
.slide{position:absolute;top:14px;width:209px}
.slide .photo{height:153px;border:1px solid #777}
.slide p{font-size:9px;line-height:12px;color:var(--light);margin-top:12px;padding-left:24px;position:relative}
.slide p::before{content:"";position:absolute;left:8px;top:3px;width:6px;height:6px;border-radius:50%;background:var(--red)}
.arrow{position:absolute;top:120px;width:0;height:0;border-top:8px solid transparent;border-bottom:8px solid transparent}
.arrow.prev{left:-12px;border-right:10px solid #ccc}
.arrow.next{right:-14px;border-left:10px solid #ccc}

/* main menu */
.menu{left:184px;top:473px;width:228px;height:321px;background:linear-gradient(90deg,#d0d0d2,#8e8e91);border:1px solid #444}
.menu h2{height:30px;background:linear-gradient(#5a5a5c,#2a2a2c);color:var(--white);font-weight:400;font-size:15px;text-align:center;line-height:30px}
.menu ul{list-style:none;padding:14px 0 0 18px}
.menu li{height:28px;border-bottom:1px solid rgba(255,255,255,.45);font-size:11px;color:#222;line-height:28px;padding-left:22px;position:relative;width:180px}
.menu li::before{content:"";position:absolute;left:4px;top:11px;width:6px;height:6px;background:#444}

/* welcome */
.welcome{left:423px;top:473px;width:635px;height:321px;background:linear-gradient(#3a1416,#231012);border:1px solid #7a2a2c;border-radius:4px}
.welcome h1{position:absolute;left:18px;top:12px;font-family:"Cinzel",serif;font-weight:700;font-size:19px;color:#e86060;letter-spacing:1px}
.welcome .pic{position:absolute;top:37px;width:139px;height:136px;border:2px solid #ddd}
.welcome .lead{position:absolute;left:17px;top:186px;width:310px;font-size:9px;line-height:12px;color:#ccc}
.welcome .notes{position:absolute;left:340px;top:34px;width:270px}
.welcome .notes p{font-size:9px;line-height:12px;color:#ddd;margin-bottom:30px;padding-left:18px;position:relative}
.welcome .notes p::before{content:"";position:absolute;left:2px;top:3px;width:7px;height:7px;border-radius:50%;background:var(--red)}
.welcome .notes p b{color:var(--red-text);font-weight:400}

/* news */
.news{left:184px;top:808px;width:874px;height:176px;background:#2b2b2d;border:1px solid #444}
.news h2{height:32px;background:linear-gradient(#dcdcde,#8d8d90);color:#222;font-size:16px;line-height:32px;padding-left:40px;position:relative;font-weight:700;border-radius:8px}
.news h2::before{content:"";position:absolute;left:10px;top:7px;width:18px;height:18px;border-radius:50%;background:#555}
.news article{margin:10px 0 0 67px;width:780px}
.news h3{font-size:9px;font-weight:400;color:var(--red-text);text-decoration:underline;margin-bottom:14px}
.news article p{font-size:9px;line-height:11px;color:#bbb}
.social{left:250px;top:952px;display:flex;gap:40px}
.social span{width:28px;height:24px;border-radius:4px;background:#6f7fa8}
.social span:nth-child(2){background:#b7b7b9}
.social span:nth-child(3){background:#8fc2dc}

.privacy{left:0;width:1200px;top:989px;text-align:center;font-size:10px;line-height:12px;color:#ddd}
.footer{left:0;top:1005px;width:1200px;height:22px;background:#0b0b0b;font-size:9px;color:#ddd;line-height:22px}
.footer .left{position:absolute;left:184px}
.footer .mid{position:absolute;left:0;width:1200px;text-align:center}
.footer .right{position:absolute;right:142px}
</style>
</head>
<body>
<div class="page">
  <nav class="nav abs">
    <a class="active">Home</a><a>Blog</a><a>Music</a><a>News Feeds</a><a>Contact Us</a>
  </nav>

  <div class="login abs">
    <div class="field">User Name</div><div class="field">Password</div>
    <div class="btn">Sign In</div><div class="btn">Sign Up</div>
  </div>

  <div class="brand abs">
    <div class="mark"></div>
    <div class="name">VELMORAN<span>RECORDS</span></div>
  </div>
  <div class="search abs">Search</div>

  <section class="slideshow abs">
    <span class="arrow prev"></span><span class="arrow next"></span>
    <div class="slide" style="left:16px">
      <div class="photo" role="img" aria-label="Artist playing acoustic guitar on stage" style="background:linear-gradient(#3a2a20,#6a4a30)"></div>
      <p>Artist biography: a short story of the songs, the stage and the road so far.</p>
    </div>
    <div class="slide" style="left:238px">
      <div class="photo" role="img" aria-label="Singer performing in a dark concert hall" style="background:linear-gradient(#1a1a1c,#4a2a24)"></div>
      <p>Artist biography: a short story of the songs, the stage and the road so far.</p>
    </div>
    <div class="slide" style="left:460px">
      <div class="photo" role="img" aria-label="Band performing live on stage" style="background:linear-gradient(#505052,#2a2a2c)"></div>
      <p>Artist biography: a short story of the songs, the stage and the road so far.</p>
    </div>
    <div class="slide" style="left:672px">
      <div class="photo" role="img" aria-label="Guitarist performing under stage lights" style="height:222px;background:linear-gradient(#6a6a6c,#3a3a3c)"></div>
    </div>
  </section>

  <aside class="menu abs">
    <h2>Main Menu</h2>
    <ul><li>HOME</li><li>BLOG</li><li>NEWS FEEDS</li><li>SEARCH</li><li>WRAPPER</li><li>MUSIC</li><li>CONTACT US</li></ul>
  </aside>

  <section class="welcome abs">
    <h1>WELCOME TO OUR WEBSITE</h1>
    <div class="pic" role="img" aria-label="Portrait of a signed artist" style="left:17px;background:linear-gradient(#e8e8e8,#9a8a80)"></div>
    <div class="pic" role="img" aria-label="Portrait of a signed artist in studio" style="left:167px;background:linear-gradient(#d8d8d8,#3a3a3a)"></div>
    <p class="lead">Velmoran is an independent label built around artists, live shows and honest recordings made with care.</p>
    <div class="notes">
      <p><b>Fresh signings join the roster</b> each season, each with a story worth hearing.</p>
      <p><b>Fresh signings join the roster</b> each season, each with a story worth hearing.</p>
      <p><b>Fresh signings join the roster</b> each season, each with a story worth hearing.</p>
    </div>
  </section>

  <section class="news abs">
    <h2>LATEST NEWS &amp; EVENTS</h2>
    <article>
      <h3>Velmoran announces its first showcase night for new artists.</h3>
      <p>Our newest artists take the stage this spring with a showcase of fresh material, live sessions and meet-and-greet moments for fans. Tickets and full details follow soon on this page.</p>
    </article>
    <article>
      <h3>Velmoran announces its first showcase night for new artists.</h3>
      <p>Our newest artists take the stage this spring with a showcase of fresh material, live sessions and meet-and-greet moments for fans. Tickets and full details follow soon on this page.</p>
    </article>
  </section>
  <div class="social abs"><span></span><span></span><span></span></div>

  <div class="privacy abs">Privacy Policies</div>
  <footer class="footer abs">
    <span class="left">Allright Reserved in 2011 (c)</span>
    <span class="mid">Home | Blog | New Feeds | Search | Music | Contact Us</span>
    <span class="right">Copyright @ VELMORAN</span>
  </footer>
</div>
</body>
</html>
```